Real Estate Company Needs a Contemporary/Modern Business Card Design

We need a Contemporary/Modern Business Card Design for a New Real Estate Company based in San Francisco, CA called Colvane Terrish Realtors. We would like to see designs that use the color red for the "Colvane Terrish" and gold for the "Realtors." The design should communicate being Modern and yet Established and Stable.

Industry/Entity Type

Business

```html
<!DOCTYPE html>
<html lang="en">
<head>
<meta charset="utf-8">
<title>Colvane Terrish Realtors – Business Card</title>
<link rel="stylesheet" href="https://fonts.googleapis.com/css2?family=Montserrat:wght@500;600;700&family=Open+Sans:wght@700&display=swap">
<style>
  :root {
    --brand-red: #d90000;
    --brand-gold: #7d6c2c;
    --paper: #ffffff;
    --page: #fdfdfd;
    --card-edge: #bdbdbd;
  }
  * { margin: 0; padding: 0; box-sizing: border-box; }
  html, body {
    width: 1200px;
    height: 849px;
    overflow: hidden;
    background: var(--page);
  }
  .canvas {
    position: relative;
    width: 1200px;
    height: 849px;
  }
  .card {
    position: absolute;
    top: 265px;
    height: 242px;
  }
  /* Front */
  .card-front {
    left: 121px;
    width: 458px;
    background: var(--brand-red);
    display: flex;
    flex-direction: column;
    align-items: center;
  }
  .front-mark {
    margin-top: 65px;
    width: 37px;
    height: 37px;
  }
  .front-name {
    margin-top: 14px;
    font-family: "Montserrat", sans-serif;
    font-weight: 600;
    font-size: 15px;
    letter-spacing: 3.6px;
    color: var(--paper);
    text-transform: uppercase;
    white-space: nowrap;
  }
  .front-rule {
    margin-top: 8px;
    width: 36px;
    height: 1.5px;
    background: var(--brand-gold);
  }
  .front-tagline {
    margin-top: 5px;
    font-family: "Montserrat", sans-serif;
    font-weight: 600;
    font-size: 12px;
    letter-spacing: 2px;
    color: var(--brand-gold);
    text-transform: uppercase;
  }
  /* Back */
  .card-back {
    left: 620px;
    width: 460px;
    background: var(--paper);
    border: 1px solid var(--card-edge);
  }
  .back-brand {
    position: absolute;
    left: 24px;
    top: 103px;
    display: flex;
    align-items: center;
    gap: 8px;
  }
  .back-mark { width: 36px; height: 36px; }
  .back-brand-name {
    font-family: "Montserrat", sans-serif;
    font-weight: 700;
    font-size: 11px;
    letter-spacing: 1.5px;
    color: var(--brand-red);
    text-transform: uppercase;
  }
  .agent-name {
    position: absolute;
    left: 24px;
    top: 153px;
    font-family: "Montserrat", sans-serif;
    font-weight: 700;
    font-size: 13px;
    letter-spacing: 1.4px;
    color: var(--brand-gold);
    text-transform: uppercase;
  }
  .contact-list {
    position: absolute;
    left: 24px;
    top: 175px;
    list-style: none;
    font-family: "Open Sans", sans-serif;
    font-weight: 700;
    font-size: 11.5px;
    line-height: 16px;
    color: var(--brand-red);
  }
</style>
</head>
<body>
<main class="canvas">
  <section class="card card-front" aria-label="Card front">
    <svg class="front-mark" viewBox="0 0 37 37" aria-hidden="true">
      <circle cx="18.5" cy="18.5" r="16.5" fill="none" stroke="var(--paper)" stroke-width="2.5"/>
    </svg>
    <h1 class="front-name">Colvane Terrish</h1>
    <div class="front-rule"></div>
    <p class="front-tagline">Realtors</p>
  </section>

  <section class="card card-back" aria-label="Card back">
    <div class="back-brand">
      <svg class="back-mark" viewBox="0 0 36 36" aria-hidden="true">
        <circle cx="18" cy="18" r="16" fill="none" stroke="var(--brand-red)" stroke-width="2.5"/>
      </svg>
      <span class="back-brand-name">Colvane Terrish</span>
    </div>
    <h2 class="agent-name">Nora Halden</h2>
    <ul class="contact-list">
      <li>2468 1357</li>
      <li>nhalden@email.com</li>
      <li>Address goes here</li>
    </ul>
  </section>
</main>
</body>
</html>
```